Insurance Law Website

**Please note do not sell insurance, we are a law firm which specialises in Insurance law.**

We are a legal insurance firm based in Australia consisting of 150+ legal professionals.

Our initial budget for this project is around: $500

We require a design to meet the specification below, however we do want designers to come up with an interpretation of something modern but still professional, we need it to stand out above all other legal websites!

1. Responsive design
2. It should be a minimalist design, the use of background imagery is fine but we are looking to de-clutter the home page in particular and have additional content accessible through menu links to other areas such as publications, news, announcements and expert/staff pages, careers etc.
3. Something that stands out from a typical legal website.
4. The homepage should cater for a video which will contain a 'who we are' message from the CEO/Firm.
5. Colours used light/medium blues (eg: #8aabff, #bdd7fc), white
6. We also require a static information box on the page with the heading "THREE STATES, ONE FOCUS" - see image attached for full text of the box.

Visitors to our website should be aware we are an Insurance law firm, this can be achieved by using insurance focused full background imagery (no natural disasters such as floods, earthquakes etc) such as insurance buildings (Harwick building - London), international landmarks etc

Some websites we like certain aspects of;

http://pellambraithwaite.com/ - top image boxes
http://www.vantel.com.au/ - similar however prefer to use a FULL background image, with one full width text box at the bottom, navigation menu at the top with logo

However please don't take these examples as a sign of what the site MUST look like, please use your imagination to interpret your own vision.

Reason: Extended due to feedback provided and waiting for resubmission of designs. It appears that some people may be misunderstanding the brief, please review the brief in full before submitting any designs and let us know if you have any questions.

Reason: Apologies to those who are waiting for a decision we are reviewing and discussiing all submitted designs internally and waiting for some additional amendments to come in. We have extended the project a final time whilst we carry out our reviews. Please continue to submit any modifications and thanks again for everyone's input thus far. D+T

We have 3 days left of this project please keep submitting your designs. This is a guaranteed project.

D+T

Target Market(s)

Lawyers looking for publications, information, contact details of our lawyers and careers/job searches.

Industry/Entity Type

Insurance

Font styles to use
Sans Serif

Requirements
Must have
• Top menu to include:

Home (small icon)
Who We Are (text)
Experts (text)
Expertise (text)
Media (text)
- News (text)
- Publications (text)
Community Footprint (text)
Careers (text)
Contact (text/icon)
Search (icon - will expand on click to search in field)

Footer to include:

Copyright (text)
Privacy Policy (text)
Cookie policy (text)
Sitemap (text)
Contact (text/icon)
Chainbook (icon)
Print (icon)
Email (icon)

Should not have
• Stereotypical imagery such as legal scales, money bags, natural disasters etc. We are a professional firm and require designs to suit.

```html
<!DOCTYPE html>
<html lang="en">
<head>
<meta charset="utf-8">
<title>Halden Marsh – Insurance Law</title>
<link rel="stylesheet" href="https://fonts.googleapis.com/css2?family=Open+Sans:wght@400&family=Pathway+Gothic+One&display=swap">
<style>
:root{
  --brand-blue:#1d4f9c;
  --link-blue:#1f4fa8;
  --accent-blue:#8aabff;
  --pale-blue:#bdd7fc;
  --text-grey:#8a8a8a;
  --white:#ffffff;
  --field-grey:#c8c8c8;
}
*{margin:0;padding:0;box-sizing:border-box}
html,body{width:1144px;height:1200px;overflow:hidden;background:var(--white)}
.page{position:absolute;left:0;top:0;width:1200px;height:1259px;transform:scale(0.9533);transform-origin:0 0;font-family:"Pathway Gothic One",sans-serif;color:var(--text-grey)}
.abs{position:absolute}

.brand{left:129px;top:40px;font-family:"Open Sans",sans-serif;color:var(--brand-blue);font-size:29px;line-height:27px;display:flex;align-items:center;gap:14px}
.brand-mark{width:12px;height:12px;border:1.5px solid var(--pale-blue)}
.contact-line{right:146px;top:40px;color:var(--brand-blue);font-size:20px;display:flex;align-items:center;gap:4px}
.search-field{left:874px;top:72px;width:183px;height:23px;background:#f3f3f3;border:1px solid #e6e6e6;font-size:13px;color:#aaa;padding:3px 4px;display:flex;justify-content:space-between;align-items:center}

.main-nav{left:131px;top:121px;display:flex;align-items:center;font-size:21px;color:var(--brand-blue)}
.main-nav span{display:block}

.hero{left:0;top:163px;width:1200px;height:533px;background:linear-gradient(180deg,#e4e4df 0%,#dcded6 35%,#b9cf7a 60%,#8fba3c 78%,#6f9a2a 100%)}
.focus-box{left:129px;top:314px;width:320px;height:232px;background:linear-gradient(120deg,rgba(255,255,255,.96) 40%,rgba(205,205,225,.9) 70%,rgba(245,245,250,.95) 100%);padding:8px 10px 0 16px;font-family:"Open Sans",sans-serif}
.focus-title{color:var(--link-blue);font-size:34px;line-height:44px;font-weight:400}
.focus-copy{margin-top:8px;font-size:15px;letter-spacing:-0.15px;line-height:22px;color:#555;text-align:justify}
.focus-copy em{font-style:normal;color:var(--accent-blue)}
.hero-search{left:130px;top:577px;width:940px;height:54px;background:var(--white);border-top:3px solid var(--field-grey);font-size:20px;color:#cfcfcf;padding:14px 18px}
.slider-dots{left:549px;top:648px;display:flex;gap:7px}
.slider-dots i{width:21px;height:21px;border-radius:50%;background:var(--white)}
.slider-dots i.active{background:var(--accent-blue)}

.section-title{top:734px;font-size:21px;color:var(--brand-blue);font-weight:400}
.welcome-photo{left:130px;top:772px;width:520px;height:160px;background:linear-gradient(90deg,#eef1f3,#dfe4e8 50%,#c8ccd0 70%,#eef0f2)}
.welcome-copy{left:132px;top:946px;width:520px;font-size:16.5px;letter-spacing:-0.3px;line-height:30px;text-align:justify}
.video{left:668px;top:772px;width:402px;height:235px;background:linear-gradient(180deg,#33547e 0%,#7d98b8 40%,#2c3e59 62%,#204b7c 75%,#163a66 100%)}
.play{left:170px;top:90px}
.video-bar{left:0;bottom:0;width:402px;height:28px;background:#161616}
.video-progress{left:0;top:0;width:402px;height:4px;background:#555}
.video-progress b{display:block;width:94px;height:4px;background:#d9272e}
.video-controls{left:10px;top:8px;width:384px;display:flex;justify-content:space-between;font-family:"Open Sans",sans-serif;font-size:7px;color:#ccc}
.who-copy{left:668px;top:1029px;width:402px;font-size:16.5px;letter-spacing:-0.3px;line-height:30px;text-align:justify}
.who-copy a{color:var(--link-blue);text-decoration:none;white-space:nowrap}

.footer{left:0;top:1175px;width:1200px;height:84px;background:var(--accent-blue);color:var(--white)}
.footer-links{left:131px;top:27px;font-size:18px;display:flex;gap:9px}
.footer-tools{left:905px;top:22px;display:flex;align-items:center;gap:14px;font-size:18px}
</style>
</head>
<body>
<div class="page">
  <header>
    <div class="abs brand"><span>Halden<br>Marsh</span><span class="brand-mark"></span></div>
    <div class="abs contact-line">
      <svg width="12" height="16" viewBox="0 0 12 16"><path d="M3 1l2 3-1.5 1.5c.5 2 2 4.5 3.5 5.5L8.5 9.5 11 12l-2 2.5C5 14 1 8 1.5 2.5z" fill="#1d4f9c"/></svg>
      <span>CONTACT US 1-300-555-0148</span>
    </div>
    <div class="abs search-field"><span>Search</span>
      <svg width="9" height="9" viewBox="0 0 9 9"><circle cx="3.5" cy="3.5" r="2.5" fill="none" stroke="#999"/><path d="M5.5 5.5L8 8" stroke="#999"/></svg>
    </div>
    <nav class="abs main-nav">
      <svg width="19" height="17" viewBox="0 0 19 17" style="margin-right:21px"><path d="M9.5 0L0 8h3v9h5v-5h3v5h5V8h3z" fill="#1d4f9c"/></svg>
      <span style="margin-right:29px">HOME</span>
      <span style="margin-right:33px">WHO WE ARE</span>
      <span style="margin-right:40px">EXPERTS</span>
      <span style="margin-right:40px">EXPERTISE</span>
      <span style="margin-right:42px">MEDIA</span>
      <span style="margin-right:25px">NEWS</span>
      <span style="margin-right:25px">PUBLICATIONS</span>
      <span style="margin-right:29px">COMMUNITY FOOTPRINT</span>
      <span>CAREERS</span>
    </nav>
  </header>

  <section class="abs hero" role="img" aria-label="Photo of a man in a shirt standing in a green grass field facing a hazy city skyline"></section>
  <div class="abs focus-box">
    <h1 class="focus-title">Three states.<br>One focus.</h1>
    <p class="focus-copy">Our sole focus is <em>insurance law</em> and we act for a diverse range of risk carriers, underwriting agents, brokers and corporate insureds relevant to litigious and general advisory services.</p>
  </div>
  <div class="abs hero-search">TYPE YOUR WORDS</div>
  <div class="abs slider-dots"><i class="active"></i><i></i><i></i><i></i></div>

  <main>
    <h2 class="abs section-title" style="left:129px">WELCOME TO HALDEN MARSH</h2>
    <div class="abs welcome-photo" role="img" aria-label="Photo of business people walking along a bright glass office corridor"></div>
    <p class="abs welcome-copy">Lorem Ipsum is simply dummy text of the printing and typesetting industry. Lorem Ipsum has been the industry's standard dummy text ever since the 1500s, when an unknown printer took a galley of type and scrambled it to make a type specimen book. It has survived not only five centuries, but also the leap into electronic typesetting, remaining essentially unchanged. It was popularised in the 1960s with the release of Letraset sheets containing Lorem Ipsum passages, and more recently with desktop publishing software like Aldus PageMaker including versions of Lorem Ipsum.</p>

    <h2 class="abs section-title" style="left:667px">WHO WE ARE ?</h2>
    <div class="abs video" role="img" aria-label="Video still of a city skyline across water at dusk">
      <svg class="abs play" width="48" height="48" viewBox="0 0 48 48"><circle cx="24" cy="24" r="22" fill="#333" fill-opacity=".75" stroke="#ddd" stroke-width="2.5"/><path d="M18 13l16 11-16 11z" fill="#fff"/></svg>
      <div class="abs video-bar">
        <div class="abs video-progress"><b></b></div>
        <div class="abs video-controls"><span>❚❚ &nbsp;◀) &nbsp;0:02 / 0:10</span><span>720p &nbsp;⤢</span></div>
      </div>
    </div>
    <p class="abs who-copy">Lorem Ipsum is simply dummy text of the printing and typesetting industry. Lorem Ipsum has been the industry's standard dummy text ever since the 1500s, when an unknown printer took a galley of type and scrambled... <a href="#">Read More</a></p>
  </main>

  <footer class="abs footer">
    <div class="abs footer-links"><span>COPYRIGHT</span><span>|</span><span>&nbsp;PRIVACY POLICY</span><span>|</span><span>COOKIE POLICY</span><span>&nbsp;|</span><span>&nbsp;SITEMAP</span></div>
    <div class="abs footer-tools">
      <span style="display:flex;align-items:center;gap:3px">
        <svg width="11" height="15" viewBox="0 0 12 16"><path d="M3 1l2 3-1.5 1.5c.5 2 2 4.5 3.5 5.5L8.5 9.5 11 12l-2 2.5C5 14 1 8 1.5 2.5z" fill="#fff"/></svg>Contact</span>
      <svg width="26" height="26" viewBox="0 0 26 26" role="img" aria-label="Chainbook"><circle cx="13" cy="13" r="12" fill="none" stroke="#fff" stroke-width="2"/></svg>
      <svg width="24" height="26" viewBox="0 0 24 26" aria-label="Print"><rect x="6" y="1" width="12" height="7" fill="#fff"/><rect x="1" y="9" width="22" height="10" rx="2" fill="#fff"/><rect x="6" y="15" width="12" height="10" fill="#fff" stroke="#8aabff" stroke-width="1.5"/></svg>
      <svg width="28" height="20" viewBox="0 0 28 20" aria-label="Email"><rect x="1" y="1" width="26" height="18" fill="none" stroke="#fff" stroke-width="1.6"/><path d="M1 1l13 10L27 1M1 19l10-9M27 19l-10-9" fill="none" stroke="#fff" stroke-width="1.6"/></svg>
    </div>
  </footer>
</div>
</body>
</html>
```